Label for flatbread

create an innovative and visually appealing label for flatbread packaging. The goal is to blend traditional bread-making heritage with a modern aesthetic that attracts consumers in retail environments while communicating freshness, quality, and authenticity.

To design a front-facing package label for flatbread that:
• Captures the essence of artisanal baking and cultural tradition.
• Stands out on shelves with strong visual appeal.
• You can use folk art to create the images on the label, elements like flatbread, wheat,
We want to print the label in a sticker and put it on bread bag, so consider that you are designing a label in a frame for instance 4 inch in 5 inch rectangular. We would like that the label has theme like the uploaded images (does not need to be similar to the uploaded images) these images give you a clue .

Target Market(s)

Groceries stores in Vancouver area Canada

Industry/Entity Type

Bakery

Font styles to use
Other font styles liked:
• feel free to choose your font yourself

Requirements
Must have
• Design the label to attract consumers and encourage them to choose this bread. Create an eye-catching label that entices consumers to try this bread. Make the label so appealing that consumers can’t resist picking up this bread.
Nice to have
• Clean, Illustration or icon of flatbread, Subtle grain (whole wheat!) or flour textures in the background to suggest craftsmanship, Made in Canada
Should not have
• we do not limit artists, use your imagination, do not put bread picture, the bread picture must be hand drawn

```html
<!DOCTYPE html>
<html lang="en">
<head>
<meta charset="UTF-8">
<title>Flat Bread Label</title>
<link href="https://fonts.googleapis.com/css2?family=Rammetto+One&family=Zilla+Slab:wght@400;700&family=Work+Sans:wght@400&display=swap" rel="stylesheet">
<style>
  :root {
    --page: #f3f2ef;
    --frame: #b5652a;
    --cream: #fdf3b5;
    --ink: #5b2c1c;
    --rule: #7a5a4a;
    --bread-light: #f6d58a;
    --bread-mid: #e7ac55;
    --bread-deep: #c9853a;
  }
  * { margin: 0; padding: 0; box-sizing: border-box; }
  html, body { width: 1200px; height: 846px; overflow: hidden; background: var(--page); }
  .canvas { position: relative; width: 1200px; height: 846px; }

  .label {
    position: absolute; left: 300px; top: 48px;
    width: 600px; height: 750px;
    background: var(--frame);
    padding: 27px;
  }
  .label__panel {
    position: relative; width: 100%; height: 100%;
    background: var(--cream);
    color: var(--ink);
  }

  .title { position: absolute; left: 0; top: 38px; width: 546px; height: 110px; }
  .title text { font-family: "Rammetto One", sans-serif; font-size: 58px; fill: var(--ink); letter-spacing: 1px; }

  .hero-bread {
    position: absolute; left: 131px; top: 150px;
    width: 290px; height: 240px;
    border-radius: 50%;
    background: radial-gradient(ellipse at 45% 40%, var(--bread-light) 0%, var(--bread-mid) 60%, var(--bread-deep) 100%);
  }

  .origin {
    position: absolute; left: 0; top: 428px; width: 100%;
    text-align: center;
    font-family: "Zilla Slab", serif; font-size: 30px; font-weight: 400;
  }

  .rule { position: absolute; border-top: 2px dashed var(--rule); }
  .rule--top { left: 39px; width: 468px; top: 496px; }
  .rule--mid { left: 39px; width: 468px; top: 571px; }
  .rule--bottom { left: 39px; width: 468px; top: 673px; }
  .rule--cell { left: 293px; width: 214px; top: 623px; }
  .rule--divider { left: 292px; top: 571px; height: 102px; border-top: none; border-left: 2px dashed var(--rule); }

  .variety {
    position: absolute; left: 0; top: 510px; width: 100%;
    text-align: center;
    font-family: "Zilla Slab", serif; font-size: 30px; font-weight: 700;
  }

  .claim-lettering {
    position: absolute; left: 108px; top: 586px;
    width: 136px; height: 72px;
    border-radius: 6px;
    background: linear-gradient(180deg, rgba(91,44,28,0.16), rgba(91,44,28,0.08));
  }

  .fact {
    position: absolute; left: 293px; width: 214px;
    text-align: center;
    font-family: "Work Sans", sans-serif; font-size: 20px; color: var(--ink);
  }
  .fact--weight { top: 583px; }
  .fact--diet { top: 635px; }
</style>
</head>
<body>
<div class="canvas">
  <div class="label">
    <div class="label__panel">
      <svg class="title" viewBox="0 0 546 110" aria-label="Flat Bread">
        <path id="title-arc" d="M 60 100 Q 273 30 486 100" fill="none"/>
        <text text-anchor="middle"><textPath href="#title-arc" startOffset="50%">FLAT BREAD</textPath></text>
      </svg>

      <div class="hero-bread" role="img" aria-label="Hand-drawn illustration of two stacked golden flatbreads"></div>

      <p class="origin">Made in Canada</p>

      <div class="rule rule--top"></div>
      <p class="variety">Whole Wheat</p>
      <div class="rule rule--mid"></div>

      <div class="claim-lettering" role="img" aria-label="Hand lettering reading No added sugar"></div>

      <div class="rule rule--divider"></div>
      <p class="fact fact--weight">7 oz. (198 g)</p>
      <div class="rule rule--cell"></div>
      <p class="fact fact--diet">Gluten-free</p>

      <div class="rule rule--bottom"></div>
    </div>
  </div>
</div>
</body>
</html>
```